Copper Hollow Sparkling

Hi all,

Thanks for taking the time to check out our brief.

Copper Hollow is an Australian wine company based in Victoria, and have been around for more than 20 years. We have a well-known sparkling Chardonnay Pinot Noir that needs a package revamp and we need your help!

Check out our current package here: http://www.copperhollowvino.com.au/our-wines/dsp-default_b.cfm?loadref=17

So here's the brief:

1. Use of the Copper Hollow logo (silhouette) and text mandatory - but can be as small/large as required.

2. Design must be shown on a sparkling bottle.

3. Can be closed with cork or crown seal - neck label/hood not mandatory.

4. Front label size to be no larger than 75mm high x 100mm wide. Back label to be no larger than 75mm x 100mm

5. Label does not have to be square/rectangular. Happy to see thoughts outside the box.

6. Design cannot be printed onto the bottle - must be on a label that can be applied to the bottle.

7. Be forward thinking. Be interesting. This design does not have to tie into our still (red and white) wine range.

8. Mandatory information to be shown on front label - a. Wine of Australia - b. Sparkling Chardonnay Pinot Noir

9. Mandatory info for front label - a. 750mL - b. Alcohol e.g. 13.5% ALC/VOL - c. Wine of Australi - d. Producer address (please insert dummy address at this stage - e. standard drinks e.g. approx 8.0 standard drinks (this can also be shown in the standard drinks glass logo) - f. space for a tasting blurb

10. Try to stay away from anything floral or overly girly.

Industry/Entity Type

Floral

Requirements
Must have
• Design must be shown on a sparkling wine bottle & include the full label design separately
Should not have
• Try to stay away from anything too floral and overly girly.

```html
<!DOCTYPE html>
<html lang="en">
<head>
<meta charset="utf-8">
<title>Copper Hollow Sparkling – Label Design</title>
<link rel="stylesheet" href="https://fonts.googleapis.com/css2?family=Questrial&family=Raleway:wght@400;500&display=swap">
<style>
  :root {
    --copper: #a96d5f;
    --copper-deep: #9a6154;
    --cream: #fbf4cc;
    --cream-soft: #efe2b4;
    --blush: #f2b6a8;
    --label-ink: #f7e2d4;
    --title-ink: #3a2a22;
    --page: #f4f2f0;
  }
  * { box-sizing: border-box; margin: 0; padding: 0; }
  html, body { width: 1200px; height: 1000px; overflow: hidden; }
  body {
    background: var(--page);
    font-family: "Raleway", sans-serif;
    position: relative;
  }

  /* Front label */
  .front-label {
    position: absolute;
    left: 50px; top: 270px;
    width: 620px; height: 465px;
    background: var(--copper);
    overflow: hidden;
  }
  .front-label__art {
    position: absolute;
    left: 95px; top: 20px;
    width: 430px; height: 390px;
    border-radius: 48% 48% 30% 30%;
    background: radial-gradient(ellipse at 50% 45%, var(--blush) 0%, rgba(242,182,168,0.75) 45%, rgba(239,226,180,0.35) 75%, rgba(169,109,95,0) 100%);
  }
  .front-label__band {
    position: absolute;
    left: 20px; right: 20px; top: 185px;
    height: 74px;
    background: var(--cream);
    text-align: center;
    color: var(--title-ink);
    font-family: "Questrial", sans-serif;
  }
  .front-label__style {
    font-size: 19px;
    letter-spacing: 1px;
    padding-top: 8px;
  }
  .front-label__variety {
    font-size: 30px;
    letter-spacing: 0.5px;
    line-height: 1.1;
  }
  .front-label__origin {
    position: absolute;
    left: 22px; bottom: 22px;
    font-size: 15px;
    color: var(--label-ink);
  }
  .front-label__brand {
    position: absolute;
    right: 22px; bottom: 22px;
    font-size: 12px;
    letter-spacing: 4px;
    color: var(--label-ink);
  }

  /* Neck band */
  .neck-band {
    position: absolute;
    left: 790px; top: 110px;
    width: 300px; height: 110px;
    background: linear-gradient(90deg, var(--copper-deep), #c88a78 50%, var(--copper-deep));
    display: flex; align-items: center; justify-content: center; gap: 10px;
  }
  .neck-band__mark {
    width: 10px; height: 10px;
    background: var(--cream-soft);
  }
  .neck-band__name {
    font-size: 13px;
    letter-spacing: 4px;
    color: var(--cream-soft);
  }

  /* Back label */
  .back-label {
    position: absolute;
    left: 730px; top: 420px;
    width: 420px; height: 315px;
    background: var(--copper);
    color: var(--label-ink);
    padding: 22px 26px;
    text-align: center;
  }
  .back-label__brand {
    display: flex; align-items: center; justify-content: center; gap: 8px;
    font-size: 11px; letter-spacing: 3px;
    margin-bottom: 8px;
  }
  .back-label__mark { width: 8px; height: 8px; background: var(--cream-soft); }
  .back-label__producer { font-size: 10px; line-height: 1.5; }
  .back-label__rule { border: 0; border-top: 1px solid rgba(247,226,212,0.55); margin: 12px 0; }
  .back-label__blurb { font-size: 11.5px; line-height: 1.5; text-align: left; }
  .back-label__facts {
    display: flex; align-items: center; justify-content: center; gap: 8px;
    font-size: 8.5px; line-height: 1.35; text-align: left;
  }
</style>
</head>
<body>
  <section class="front-label" aria-label="Front label">
    <div class="front-label__art" role="img" aria-label="Illustration of a sparkling wine glass crossed by two bottles"></div>
    <div class="front-label__band">
      <p class="front-label__style">SPARKLING</p>
      <p class="front-label__variety">CHARDONNAY PINOT NOIR</p>
    </div>
    <p class="front-label__origin">Wine of Australia</p>
    <p class="front-label__brand">COPPER HOLLOW</p>
  </section>

  <section class="neck-band" aria-label="Neck label">
    <span class="neck-band__mark"></span>
    <span class="neck-band__name">COPPER HOLLOW</span>
  </section>

  <section class="back-label" aria-label="Back label">
    <p class="back-label__brand"><span class="back-label__mark"></span>COPPER HOLLOW</p>
    <p class="back-label__producer">Wine of Australia<br>Name Street, Town 5230 City</p>
    <hr class="back-label__rule">
    <p class="back-label__blurb">Lorem ipsum dolor sit amet, consectetur adipiscing elit. Cras sit amet vehicula risus. Nam viverra nulla risus, at ultricies urna porta at. In eu sagittis quam. Phasellus vitae erat non lacus aliquam.</p>
    <hr class="back-label__rule">
    <div class="back-label__facts">
      <svg width="16" height="22" viewBox="0 0 16 22" aria-hidden="true">
        <path d="M2 1h12l-1 7a5 5 0 0 1-10 0z M8 13v6 M4 21h8" fill="none" stroke="#f7e2d4" stroke-width="1.3"/>
      </svg>
      <p>approx 8.0 standard drinks<br>750mL<br>ALC 13.5% VOL</p>
    </div>
  </section>
</body>
</html>
```